Maplerise Trading Inc. needs an innovative idea for letterhead and visiting cards.

Maplerise Trading Inc. is a Canadian brand since 2007. It is a renown dealer of kids and office furniture locally. Moreover, exporting electric fixtures e.g. switches, LED's, down-lights etc. to Middle East and Africa. We have initiated a number of steps including re-branding, to boost our export in 2020. We have successfully designed our new logo a few months ago through 'Artfolio' and now we are looking for an innovative idea for a letterhead.
Some key points:
• Red, black and white are the three colors used in all our packaging and furniture. (grey is optional)
• Shouldn’t be too wide.
• Use of watermark is preferable.
• You can visit our North American site at www.mapleriseinc.com. Export website of the company will be launched soon. www.mapleriseinc.ca
• Same letterhead will be used locally and internationally.
• Our new logo and sample packaging is attached.

```html
<!DOCTYPE html>
<html lang="en">
<head>
<meta charset="utf-8">
<title>Maplerise Trading – Business Card</title>
<link href="https://fonts.googleapis.com/css2?family=Questrial&display=swap" rel="stylesheet">
<style>
  :root {
    --brand-red: #a3161c;
    --ink: #3a3a3a;
    --paper: #ffffff;
    --canvas: #ffffff;
    --card-dark-top: #4a4a4a;
    --card-dark-bottom: #2d2d2d;
    --outline: #e4e4e4;
  }
  * { margin: 0; padding: 0; box-sizing: border-box; }
  html, body {
    width: 1200px; height: 840px; overflow: hidden;
    background: var(--canvas);
    font-family: "Questrial", sans-serif;
    color: var(--ink);
  }
  .stage { position: relative; width: 1200px; height: 840px; }
  .card {
    position: absolute; top: 232px;
    width: 364px; height: 364px; border-radius: 10px;
    overflow: hidden;
  }
  .card--front { left: 204px; background: var(--paper); border: 1px solid var(--outline); }
  .card--back {
    left: 632px;
    background: linear-gradient(180deg, var(--card-dark-top), var(--card-dark-bottom));
  }

  .brand {
    position: absolute; left: 34px; top: 40px;
    color: var(--brand-red); font-size: 29px; line-height: 33px;
    letter-spacing: 1px; text-transform: uppercase;
  }

  .person { position: absolute; left: 34px; top: 152px; }
  .person__name { color: var(--brand-red); font-size: 18px; letter-spacing: 1.2px; text-transform: uppercase; line-height: 20px; }
  .person__role { font-size: 13px; margin-top: 4px; }

  .rule { position: absolute; left: 34px; width: 26px; height: 2px; background: var(--brand-red); }
  .rule--one { top: 202px; }
  .rule--two { top: 266px; }

  .address { position: absolute; left: 34px; top: 216px; font-size: 13px; line-height: 18px; font-style: normal; }

  .contacts { position: absolute; left: 34px; top: 281px; list-style: none; font-size: 13px; }
  .contacts li { display: flex; align-items: center; height: 17.6px; }
  .contacts svg { width: 10px; height: 10px; margin-right: 6px; flex: none; }

  .back-name {
    position: absolute; inset: 0;
    display: flex; align-items: center; justify-content: center; text-align: center;
    color: var(--paper); font-size: 34px; line-height: 42px;
    letter-spacing: 2px; text-transform: uppercase;
  }
</style>
</head>
<body>
<main class="stage">
  <section class="card card--front">
    <div class="brand">Maplerise<br>Trading</div>

    <div class="person">
      <div class="person__name">Daniel Whitford</div>
      <div class="person__role">Director</div>
    </div>
    <div class="rule rule--one"></div>

    <address class="address">
      84 Alderwood Ave,<br>Unit 207, Maple Grove
    </address>
    <div class="rule rule--two"></div>

    <ul class="contacts">
      <li>
        <svg viewBox="0 0 10 10"><path d="M2 0.5 L3.6 0.5 L4.2 2.8 L3 3.6 Q4 6 6.4 7 L7.2 5.8 L9.5 6.4 L9.5 8 Q9.5 9.5 8 9.5 Q1 8.5 0.5 2 Q0.5 0.5 2 0.5 Z" fill="var(--brand-red)"/></svg>
        +1 (888) 555-0142
      </li>
      <li>
        <svg viewBox="0 0 10 10"><rect x="0.7" y="2" width="8.6" height="6" rx="0.8" fill="none" stroke="var(--brand-red)" stroke-width="1.2"/><path d="M1 2.4 L5 5.4 L9 2.4" fill="none" stroke="var(--brand-red)" stroke-width="1.1"/></svg>
        sales@mapleriseinc.com
      </li>
      <li>
        <svg viewBox="0 0 10 10"><g fill="none" stroke="var(--brand-red)" stroke-width="0.9"><circle cx="5" cy="5" r="4.3"/><ellipse cx="5" cy="5" rx="1.9" ry="4.3"/><path d="M0.7 5 H9.3 M1.4 2.8 H8.6 M1.4 7.2 H8.6"/></g></svg>
        www.mapleriseinc.com
      </li>
    </ul>
  </section>

  <section class="card card--back">
    <div class="back-name">Maplerise<br>Trading</div>
  </section>
</main>
</body>
</html>
```